Plakat-Design
Zielgruppe
Wir sind eine Firma mit zwei verschiedenen Bereichen.
Der eine Bereich ist Onlinehandel unter dem Namen Kuno-Form ( www.kuno-form.de ) und der andere Bereich sind technische Dienstleistungen unter dem Namen RKLV - technische Dienstleistungen.
Aufgabenstellung
Wir benötigen ein Design für ein Werbebanner oder ein Firmenschild für den Außenbereich.
Darauf sollten folgende Punkte enthalten sein:
- Der Firmenname oder das Logo Kuno-Form.de und der Firmenname RKLV (kein Logo vorhanden) .
- Der Straßenname Bingelauer Str. 27
- Der Standort wo das Schild hängt und der Standort wo die Anlieferung und Abholung ist ( in Deutsch und Englisch )
Wir liegen sehr versteckt und die Lieferfahrzeuge (oft aus Polen ohne Deutschkenntnisse ) sollen sofort erkennen wo sie hin müssen. Auf deren Abholschein steht nur RKLV.
Wir haben auch schon mal etwas vorab gestaltet was unser anliegen beschreibt.
Die Maße müssen wir noch genau festlegen für den späteren Druck.
Wahrscheinlich wir es 1 Meter breit und 2,5 Meter hoch.

```html
<!DOCTYPE html>
<html lang="de">
<head>
<meta charset="utf-8">
<title>RKLV – Firmenschild</title>
<link rel="stylesheet" href="https://fonts.googleapis.com/css2?family=Lato:wght@300;400;700;900&display=swap">
<style>
  :root {
    --backdrop: #e9eaec;
    --frame: #3d4247;
    --brand-blue: #0a8fd3;
    --white: #ffffff;
    --panel-grey: #ececec;
    --ink: #111111;
    --text-dark: #2b2b2b;
    --logo-grey: #8a8a8a;
    --map-grey: #5a5a5a;
    --pin-red: #d8141f;
  }
  * { box-sizing: border-box; margin: 0; padding: 0; }
  html, body {
    width: 1080px; height: 1200px; overflow: hidden;
    background: var(--backdrop);
    font-family: "Lato", Arial, sans-serif;
  }
  .canvas {
    width: 1080px; height: 1200px;
    display: flex; align-items: center; justify-content: center;
  }
  .sign {
    width: 460px; height: 1150px;
    background: var(--frame);
    padding: 12px;
    display: flex; flex-direction: column;
  }
  .sign__band { width: 100%; }
  .divider { height: 8px; background: var(--ink); }
  .divider--blue { background: var(--brand-blue); }

  .company {
    height: 260px; background: var(--brand-blue); color: var(--white);
    padding: 42px 26px 0;
  }
  .company__name {
    font-weight: 700; font-size: 132px; line-height: 1; letter-spacing: 2px;
  }
  .company__tagline {
    font-weight: 400; font-size: 25px; margin-top: 14px; letter-spacing: -0.2px;
  }

  .shop {
    height: 140px; background: var(--white);
    display: flex; align-items: center; justify-content: center; gap: 14px;
  }
  .shop__name {
    font-weight: 300; font-size: 50px; color: var(--brand-blue); letter-spacing: 0.5px;
  }
  .shop__dot {
    width: 30px; height: 30px; border-radius: 50%; background: var(--logo-grey);
    align-self: flex-start; margin-top: 34px;
  }

  .directions {
    height: 520px; background: var(--panel-grey); position: relative;
    padding: 22px 22px 0;
  }
  .directions__labels {
    text-align: right; font-weight: 700; font-size: 25px; line-height: 1.22;
    color: var(--text-dark);
  }
  .site-map {
    position: absolute; left: 40px; right: 24px; top: 150px; height: 240px;
    background: linear-gradient(180deg, #5e5e5e, #4a4a4a);
  }
  .position-label {
    position: absolute; left: 22px; bottom: 24px;
    font-weight: 700; font-size: 27px; line-height: 1.2; color: var(--text-dark);
  }

  .address {
    height: 182px; background: var(--ink); color: var(--white);
    padding: 40px 24px 0; font-weight: 700; font-size: 34px; line-height: 1.3;
  }
</style>
</head>
<body>
<main class="canvas">
  <section class="sign">
    <header class="sign__band company">
      <h1 class="company__name">RKLV</h1>
      <p class="company__tagline">Technische Dienstleistungen</p>
    </header>
    <div class="divider"></div>
    <div class="sign__band shop">
      <span class="shop__name">Kuno-Form.de</span>
      <span class="shop__dot"></span>
    </div>
    <div class="divider"></div>
    <div class="sign__band directions">
      <p class="directions__labels">
        Anlieferung – Abholung<br>
        Delivery – Pick up<br>
        Büro – Office
      </p>
      <div class="site-map" role="img" aria-label="Lageplan der Gebäude mit Weg vom Standort des Schildes zur Anlieferung"></div>
      <p class="position-label">Standort<br>Position</p>
    </div>
    <div class="divider divider--blue"></div>
    <footer class="sign__band address">
      <p>Bingelauer Straße 27</p>
      <p>Tel. 05531 48 20 317</p>
    </footer>
  </section>
</main>
</body>
</html>
```